Design Tweak needed for a current site

Design on top of an existing quiz funnel

Ideally we would like to tweak what we have already built here (moving elements, styles, adding simple elements etc): http://offers.rateplumfinder.com/could-you-cut-your-auto-premium

The flow:
1) User lands on the quiz page
2) User answers X questions and moves through the flow
3) Calculating user results screen
4) User reaches a success screen, and is subsequently redirected

Keys to the design:
1) We need to emphasize the quiz title as that will drive engagement. In this case, this is a quiz to see if you might be eligible to save money on car insurance.

2) At the end of the quiz we need to make it very, very clear that the user is eligible for savings and that in order to complete the process they are being redirected to another page where they need to fill out a form. It is critical that the design communicates this very clearly... We can count down the time left until redirect and we can use any order of elements to make this point. I think our current design does a very bad job of this.

3) We want to have a "calculating" step so that it seems like the page is working in the background

Goals of the design:
1) Polished, high quality experience throughout
2) User is clearly prepared to be redirected to the conversion funnel/landing page at the end
3) User understands the value of completing the quiz

Target Market(s)

designers

Industry/Entity Type

Moving

Number of Pages Required

1 page

Font styles to use
Sans Serif

Colors

Designer to choose colors to be used in the design.

Requirements
Must have
• This quiz funnel is a template so while the current use case is for auto insurance, we would like a design that also would work in other contexts.
Should not have
• We don't want to materially change the core functionality of the quiz itself... redesigning any of the elements or interactions is encouraged though

```html
<!DOCTYPE html>
<html lang="en">
<head>
<meta charset="utf-8">
<title>RatePlumFinder – Car Insurance Quiz</title>
<link href="https://fonts.googleapis.com/css2?family=Open+Sans:wght@400;700&family=Nunito+Sans:wght@400;600&display=swap" rel="stylesheet">
<style>
  :root {
    --ink: #000000;
    --text: #222222;
    --muted: #333333;
    --rule: #dddddd;
    --header-line: #d6d6d6;
    --step-idle: #ebebeb;
    --step-line: #e6e6e6;
    --card-border: #d9d9d9;
    --icon-fill: #1a1a1a;
    --bg: #ffffff;
  }
  * { box-sizing: border-box; margin: 0; padding: 0; }
  html, body { width: 1200px; height: 754px; overflow: hidden; background: var(--bg); }
  body { position: relative; font-family: "Nunito Sans", sans-serif; color: var(--text); }

  .site-header {
    position: absolute; left: 0; top: 0; width: 1200px; height: 76px;
    border-bottom: 1px solid var(--header-line);
    display: flex; align-items: center; justify-content: center; gap: 8px;
  }
  .brand-dot { width: 29px; height: 29px; border-radius: 50%; background: var(--ink); }
  .brand-name { font-family: "Nunito Sans", sans-serif; font-weight: 600; font-size: 26px; color: var(--muted); letter-spacing: 0.2px; }

  .quiz-intro {
    position: absolute; left: 234px; top: 122px; width: 704px; height: 109px;
    border-top: 3px solid var(--rule); border-bottom: 3px solid var(--rule);
    text-align: center;
  }
  .quiz-title {
    font-family: "Open Sans", sans-serif; font-weight: 700; font-size: 35px;
    color: var(--ink); margin-top: 10px; line-height: 44px; letter-spacing: -0.2px;
  }
  .quiz-subtitle { font-size: 13.5px; margin-top: 10px; color: var(--muted); }

  .stepper { position: absolute; left: 0; top: 282px; width: 1200px; height: 48px; }
  .step-line { position: absolute; top: 23px; height: 2px; background: var(--step-line); }
  .step-line.done { background: var(--ink); }
  .step {
    position: absolute; top: 0; width: 47px; height: 47px; border-radius: 50%;
    background: var(--step-idle); color: var(--muted);
    display: flex; align-items: center; justify-content: center;
    font-family: "Open Sans", sans-serif; font-size: 15px;
  }
  .step.active { background: var(--ink); color: #fff; font-weight: 700; }

  .step-label { position: absolute; left: 0; top: 346px; width: 1200px; text-align: center; font-family: "Open Sans", sans-serif; font-size: 10.5px; color: var(--ink); }

  .question { position: absolute; left: 0; top: 408px; width: 1200px; text-align: center; font-size: 19.5px; color: var(--ink); }

  .answer {
    position: absolute; top: 474px; width: 151px; height: 159px;
    border: 1px solid var(--card-border); text-align: center;
  }
  .answer-icon { display: block; margin: 27px auto 0; background: var(--icon-fill); }
  .answer-icon.lease { width: 46px; height: 57px; }
  .answer-icon.own { width: 68px; height: 52px; margin-top: 29px; }
  .answer-label { position: absolute; left: 0; top: 108px; width: 100%; font-size: 16.5px; color: var(--ink); }

  .site-footer { position: absolute; left: 0; top: 694px; width: 1200px; text-align: center; font-size: 10.5px; color: var(--muted); }
</style>
</head>
<body>
  <header class="site-header">
    <span class="brand-dot"></span>
    <span class="brand-name">RatePlumFinder</span>
  </header>

  <section class="quiz-intro">
    <h1 class="quiz-title">Quiz: Are You Overpaying For Car Insurance?</h1>
    <p class="quiz-subtitle">Take our five question quiz to see if you might be eligible for car insurance savings</p>
  </section>

  <div class="stepper">
    <div class="step-line done" style="left:410px;width:84px;"></div>
    <div class="step-line" style="left:514px;width:256px;"></div>
    <div class="step active" style="left:364px;">1</div>
    <div class="step" style="left:469px;">2</div>
    <div class="step" style="left:575px;">3</div>
    <div class="step" style="left:678px;">4</div>
    <div class="step" style="left:771px;">5</div>
  </div>
  <p class="step-label">Question 1/5</p>

  <h2 class="question">Do you Lease or Own</h2>

  <div class="answer" style="left:428px;">
    <span class="answer-icon lease" role="img" aria-label="Icon of a lease contract with a car and dollar sign"></span>
    <span class="answer-label">I Lease!</span>
  </div>
  <div class="answer" style="left:607px;">
    <span class="answer-icon own" role="img" aria-label="Icon of an owner standing beside a car"></span>
    <span class="answer-label">I Own!</span>
  </div>

  <footer class="site-footer">Copyrights @ 2017 All Rights Reserved</footer>
</body>
</html>
```